Business card design for new eCommerce site focusing on integrity and strong businsess tactics

We need a business card that will stand out and be memorable. Something with color that matches our company logo colors. Think high end version of Dealvine. There are 2 logos provided. The parent company is called Bright Harbor Ventures and we are presenting a new and very exciting eCommerce site called KeenTraders.example.

Target Market(s)

Our target markets are in the Activities, Food and Beverage, Health and Beauty

Industry/Entity Type

Marketing

Contact Information for Business Card

We have 4 members that need cards...I will provide all info to the winner of the design contest
Business Address is
48730 West 61st Avenue, Suite C204
Phoenix AZ 85917

Font styles to use
Serif
Sans Serif

Colors

Designer to choose colors to be used in the design.

Requirements
Must have
• The card must be memorable...should be unique in design but must exude integrity and be playful .
• I have provided several colors or our parent company...please feel free to use which ever
Nice to have
• I will leave this up to you. Feel free to use other images of your choosing that wraps around our client.....Activities, Dining, Health, Beauty
Should not have
• just dont be boring

```html
<!DOCTYPE html>
<html lang="en">
<head>
<meta charset="utf-8">
<title>Bright Harbor Ventures – Business Card</title>
<link rel="stylesheet" href="https://fonts.googleapis.com/css2?family=Cormorant+Garamond:wght@500&family=Open+Sans:wght@400;600;700&display=swap">
<style>
  :root {
    --stage: #2b3031;
    --card: #141414;
    --lime: #8dc63f;
    --lime-soft: #e2ebc3;
    --text-light: #e6e6e6;
    --text-muted: #b9b9b9;
    --text-dark: #444444;
    --brand-blue: #2a6fb0;
  }
  * { box-sizing: border-box; margin: 0; padding: 0; }
  html, body { width: 1200px; height: 1000px; overflow: hidden; }
  body {
    background: var(--stage);
    font-family: "Open Sans", Arial, sans-serif;
    display: flex; flex-direction: column; align-items: center; justify-content: center; gap: 30px;
  }
  .card {
    position: relative; width: 800px; height: 457px; overflow: hidden;
    background: linear-gradient(160deg, #1d1d1d 0%, var(--card) 60%, #0e0e0e 100%);
    box-shadow: 0 18px 40px rgba(0,0,0,.45);
  }
  .brand-mark { display: flex; align-items: center; gap: 10px; color: var(--lime); font-weight: 700; }
  .brand-mark .dot { width: 16px; height: 16px; border-radius: 50%; background: var(--lime); }

  /* Front */
  .front .brand-mark { position: absolute; left: 60px; top: 46px; font-size: 22px; }
  .front .address { position: absolute; left: 60px; top: 130px; color: var(--text-light); font-size: 19px; line-height: 1.5; }
  .front .contacts { position: absolute; left: 60px; top: 228px; list-style: none; color: var(--text-light); font-size: 17px; }
  .front .contacts li { display: flex; align-items: center; gap: 12px; margin-bottom: 10px; }
  .front .contacts svg { width: 18px; height: 18px; flex: none; }
  .front .identity { position: absolute; right: 56px; top: 96px; }
  .front .person { font-family: "Cormorant Garamond", Georgia, serif; font-weight: 500; color: var(--lime); font-size: 42px; letter-spacing: 1px; line-height: 1; }
  .front .role { color: var(--text-light); font-size: 21px; margin-top: 8px; }
  .front .arc { position: absolute; inset: 0; }

  .client { position: absolute; }
  .client-name { font-size: 26px; font-weight: 600; color: var(--brand-blue); display: flex; align-items: center; gap: 10px; line-height: 1.2; }
  .client-name .dot { width: 14px; height: 14px; border-radius: 50%; background: var(--lime); }
  .client-tagline { font-size: 14px; margin-top: 4px; padding-left: 24px; letter-spacing: .3px; }
  .front .client { left: 455px; top: 322px; }
  .front .client-tagline { color: var(--text-dark); }

  /* Back */
  .back .brand-mark { position: absolute; left: 0; right: 0; top: 34px; justify-content: center; font-size: 24px; }
  .back .photo-band {
    position: absolute; left: 0; right: 0; top: 100px; height: 220px;
    border-top: 10px solid var(--lime); border-bottom: 10px solid var(--lime);
    display: flex;
  }
  .photo { flex: 1; }
  .photo.dining { background: linear-gradient(135deg, #6b3a2a, #a87a5c 60%, #4a2a22); }
  .photo.spa { background: linear-gradient(135deg, #c9a46a, #e8d7b8 55%, #b38a52); }
  .photo.wine { background: linear-gradient(135deg, #9a7a55, #6d7a3a 50%, #d8c7a6); }
  .back .client { right: 50px; top: 352px; }
  .back .client-tagline { color: var(--text-muted); }
</style>
</head>
<body>

<section class="card front" aria-label="Business card front">
  <svg class="arc" viewBox="0 0 800 457" aria-hidden="true">
    <circle cx="760" cy="620" r="444" fill="#ffffff"/>
    <circle cx="760" cy="620" r="438" fill="var(--lime)"/>
    <circle cx="760" cy="620" r="424" fill="var(--lime-soft)"/>
  </svg>

  <div class="brand-mark"><span class="dot"></span>Bright Harbor Ventures</div>

  <p class="address">48730 West 61st Avenue, Suite C204<br>Phoenix AZ 85917</p>

  <ul class="contacts">
    <li>
      <svg viewBox="0 0 24 24" aria-hidden="true"><path fill="var(--lime)" d="M6.6 10.8a15.2 15.2 0 0 0 6.6 6.6l2.2-2.2a1 1 0 0 1 1-.25 11.4 11.4 0 0 0 3.6.57 1 1 0 0 1 1 1V20a1 1 0 0 1-1 1A17 17 0 0 1 3 4a1 1 0 0 1 1-1h3.5a1 1 0 0 1 1 1c0 1.25.2 2.45.57 3.57a1 1 0 0 1-.25 1z"/></svg>
      (555) 014-2290
    </li>
    <li>
      <svg viewBox="0 0 24 24" aria-hidden="true"><rect x="2" y="5" width="20" height="14" rx="1" fill="none" stroke="var(--lime)" stroke-width="2"/><path d="M2 6l10 7 10-7" fill="none" stroke="var(--lime)" stroke-width="2"/></svg>
      info@brightharbor.example
    </li>
    <li>
      <svg viewBox="0 0 24 24" aria-hidden="true"><circle cx="12" cy="12" r="10" fill="var(--lime)"/></svg>
      brightharbor.example
    </li>
  </ul>

  <div class="identity">
    <p class="person">MARA DELLWYN</p>
    <p class="role">Job Title</p>
  </div>

  <div class="client">
    <p class="client-name"><span class="dot"></span>KeenTraders.example</p>
    <p class="client-tagline">Play-Taste-Wellness-Glow</p>
  </div>
</section>

<section class="card back" aria-label="Business card back">
  <div class="brand-mark"><span class="dot"></span>Bright Harbor Ventures</div>

  <div class="photo-band">
    <div class="photo dining" role="img" aria-label="Photo of a restaurant table set with glasses"></div>
    <div class="photo spa" role="img" aria-label="Photo of a bright wooden spa lounge with cushions"></div>
    <div class="photo wine" role="img" aria-label="Photo of wine glasses with grapes and barrels"></div>
  </div>

  <div class="client">
    <p class="client-name"><span class="dot"></span>KeenTraders.example</p>
    <p class="client-tagline">Play-Taste-Wellness-Glow</p>
  </div>
</section>

</body>
</html>
```